Fox & Fern honey company needs a label design.

We need a label design for a new honey company, based in the state of Florida called 'Fox & Fern". We are supplying our online customers with the highest quality of the various kinds of raw honey. Our product is honey in the oval hexagon glass jar with black lid. We would like to see designs that use black background with gold font .
In the upper part of the label is gold flying Honey Bee (profile, silhouette). The name of the brand "Fox & Fern" - Caramel font. Additional fonts are Cinzel, Source Sans Pro. Label measurements 2.6" by 3".
Label content:
Fox & Fern
RAW HONEY
wildflower
PURE & NATURAL
made by Florida Bees
foxandfernhoney.com
NET WT 12oz (340g)

The final design should have eye catching, luxurious look.
Updates

Target Market(s)

Luxury

Industry/Entity Type

Food (bee products)

Other font styles liked:
• caramel

Colors

Designer to choose colors to be used in the design.

Requirements
Must have
• Gold letters on black background, Drawing of a bee, flying in profile

```html
<!DOCTYPE html>
<html lang="en">
<head>
<meta charset="UTF-8">
<title>Fox &amp; Fern Honey Labels</title>
<link rel="stylesheet" href="https://fonts.googleapis.com/css2?family=Cinzel:wght@400;600;700&family=Source+Sans+3:wght@300;400;600&display=swap">
<style>
  :root {
    --page-bg: #d9d9d9;
    --label-black: #0b0807;
    --label-deep: #150d08;
    --glow-amber: #6a2f08;
    --gold: #d9b15f;
    --gold-light: #ecd08f;
    --gold-soft: #c9a45c;
  }
  * { margin: 0; padding: 0; box-sizing: border-box; }
  html, body {
    width: 1200px;
    height: 980px;
    overflow: hidden;
    background: var(--page-bg);
  }
  .canvas {
    position: relative;
    width: 1200px;
    height: 980px;
    display: flex;
    justify-content: center;
    align-items: center;
    gap: 120px;
  }
  .label {
    position: relative;
    width: 440px;
    height: 510px;
    border-radius: 14px;
    overflow: hidden;
    background:
      radial-gradient(ellipse 60% 55% at 50% 45%, var(--label-black) 40%, transparent 100%),
      linear-gradient(90deg, var(--glow-amber) 0%, var(--label-deep) 22%, var(--label-black) 50%, var(--label-deep) 78%, var(--glow-amber) 100%);
    text-align: center;
    color: var(--gold);
  }
  .label__texture {
    position: absolute;
    inset: 0;
    background: linear-gradient(180deg, rgba(120, 55, 10, 0.18), rgba(0, 0, 0, 0) 40%, rgba(120, 55, 10, 0.14));
  }
  .label__content {
    position: relative;
    display: flex;
    flex-direction: column;
    align-items: center;
    height: 100%;
    padding-top: 44px;
  }
  .brand-name {
    font-family: 'Cinzel', serif;
    font-weight: 600;
    font-size: 40px;
    letter-spacing: 1px;
    color: var(--gold);
    line-height: 1;
  }
  .bee-art {
    display: block;
    margin-top: 26px;
    width: 88px;
    height: 74px;
  }
  .divider {
    width: 112px;
    height: 3px;
    margin-top: 30px;
    background: var(--gold-soft);
  }
  .product-title {
    margin-top: 28px;
    font-family: 'Cinzel', serif;
    font-weight: 700;
    font-size: 40px;
    color: var(--gold-light);
    line-height: 1;
  }
  .variety {
    margin-top: 28px;
    font-family: 'Cinzel', serif;
    font-weight: 700;
    font-size: 27px;
    color: var(--gold-light);
    line-height: 1;
  }
  .tagline {
    margin-top: 10px;
    font-family: 'Cinzel', serif;
    font-weight: 400;
    font-size: 16px;
    color: var(--gold);
    letter-spacing: 0.5px;
  }
  .origin {
    margin-top: 34px;
    font-family: 'Source Sans 3', sans-serif;
    font-weight: 300;
    font-size: 16px;
    color: var(--gold);
  }
  .origin__sep { padding: 0 6px; }
  .net-weight {
    margin-top: 22px;
    font-family: 'Source Sans 3', sans-serif;
    font-weight: 600;
    font-size: 13px;
    color: var(--gold-light);
  }
  .net-weight__small { font-size: 10px; }
</style>
</head>
<body>
<main class="canvas">

  <section class="label">
    <div class="label__texture"></div>
    <div class="label__content">
      <h1 class="brand-name">Fox &amp; Fern</h1>
      <svg class="bee-art" viewBox="0 0 88 74" role="img" aria-label="Gold engraved honey bee in flight, profile view">
        <defs>
          <radialGradient id="beeGlowA" cx="50%" cy="50%" r="50%">
            <stop offset="0%" stop-color="#d9b15f" stop-opacity="0.9"/>
            <stop offset="100%" stop-color="#d9b15f" stop-opacity="0"/>
          </radialGradient>
        </defs>
        <ellipse cx="44" cy="37" rx="44" ry="37" fill="url(#beeGlowA)"/>
      </svg>
      <div class="divider"></div>
      <h2 class="product-title">RAW HONEY</h2>
      <p class="variety">WILDFLOWER</p>
      <p class="tagline">PURE &amp; NATURAL</p>
      <p class="origin">made by Florida Bees<span class="origin__sep">|</span>foxandfernhoney.com</p>
      <p class="net-weight">NET <span class="net-weight__small">WT.</span> 12oz (340g)</p>
    </div>
  </section>

  <section class="label">
    <div class="label__texture"></div>
    <div class="label__content">
      <h1 class="brand-name">Fox &amp; Fern</h1>
      <svg class="bee-art" viewBox="0 0 88 74" role="img" aria-label="Gold engraved honey bee in flight, profile view">
        <defs>
          <radialGradient id="beeGlowB" cx="50%" cy="50%" r="50%">
            <stop offset="0%" stop-color="#d9b15f" stop-opacity="0.9"/>
            <stop offset="100%" stop-color="#d9b15f" stop-opacity="0"/>
          </radialGradient>
        </defs>
        <ellipse cx="44" cy="37" rx="44" ry="37" fill="url(#beeGlowB)"/>
      </svg>
      <div class="divider"></div>
      <h2 class="product-title">GALLBERRY</h2>
      <p class="variety">WILDFLOWER</p>
      <p class="tagline">PURE &amp; NATURAL</p>
      <p class="origin">made by Florida Bees<span class="origin__sep">|</span>foxandfernhoney.com</p>
      <p class="net-weight">NET <span class="net-weight__small">WT.</span> 12oz (340g)</p>
    </div>
  </section>

</main>
</body>
</html>
```